International Marketing Company - Web Design Project

kVesta is a well-funded start up in London developing an Online Marketing Platform for small businesses in Europe.

We require a large number of high quality business web designs for our business website builder. Our business websites are completely integrated into our Online Marketing systems and therefore it is important for designers to comply with our Design Guidelines.

This initial contest is a trial for us to open up the design process to top designers for the Builders vertical (e.g. Builders, Electricians, Plumbers, Flooring, etc.). We have implemented a base html structure and design and included them in the files.

Use your creativity to design new and fresh designs based on the included elements (e.g. testimonials, business description, etc).

We will award the stated prize money for the top three designs.

Any designers that submit designs we feel are of a high enough quality but do not make the top 3 could still be compensated and WILL be invited to participate in our next vertical competition.

Therefore, we encourage designers to submit as many designs as possible as we may award up to 25 designs.

Submissions will be reviewed daily and feedback provided where possible.

Designers who can also code will have the options to implement their designs for an additional fee.

Good luck!
Updates

There has been a mistake made in regard to the prize. Pixel Harbor should have it fixed soon.

1st place = £350
2nd place = £250
3rd Place = £150

Thanks,
Dorian
25/11/2011

UPDATE:

1st place will win £350
2nd place will win £250
3rd place will win £150

Everything else is as to the specification.

Thanks
Dorian

Target Market(s)

Builders, Electricians, Plumbers, Tradesman, Small construction companies

Industry/Entity Type

Business

Requirements
Must have
• Totally new designs based around the elements we want to show on each page.

We are looking for something different to the design we already have. But you can use that as a starting point.

Use the included files to see what is required for each page. Here is a brief outline:

Homepage - Testimonials, News, Business Description, Latest Projects and Call to action

About-Us - Team Summary, About the Business and a call to action

Projects Page - Project Details (Oage Title and description), Each project needs a title, content and 2 images.

Testimonials Page - The testifiers name and their comment

Contacts Page - Trovix Map, Company address, business hours, contact form and a call to action.

Please submit final designs in Photoshop or Fireworks format.

Each page has a set of elements. These element must feature in the design of that page. See supporting documents for page details.

All elements must be included in your design. Please do not add any extra element.

Professional look and feel
Nice to have
• Design variations:
Full width designs
Boxed Designs
With AND without carousels
OR static images
Good use of stock images.

Creative use of the elements, dont be restricted/influenced by the default design we have already

Designs based on the 960 grid

```html
<!DOCTYPE html>
<html lang="en">
<head>
<meta charset="utf-8">
<title>Kestrel Builders – Home</title>
<link href="https://fonts.googleapis.com/css2?family=Arimo:ital,wght@0,400;0,700;1,700&display=swap" rel="stylesheet">
<style>
:root{
  --top-band:#333333;
  --hero-red:#a8323e;
  --hero-red-dark:#8e2631;
  --page-grey:#7b7b7b;
  --footer-brown:#4b1c0c;
  --header-brown:#5a2412;
  --welcome-orange:#f07a12;
  --tab-blue:#2f79c9;
  --tab-red:#b83a3f;
  --cream:#efe8d9;
  --panel-grey:#e3e3e3;
  --text:#333333;
  --accent-red:#b02a35;
  --link-blue:#1f5fb0;
}
*{margin:0;padding:0;box-sizing:border-box}
html,body{width:1200px;height:1029px;overflow:hidden}
body{position:relative;background:var(--page-grey);font-family:"Arimo",Arial,sans-serif;color:var(--text)}
.abs{position:absolute}
.band-top{left:0;top:0;width:1200px;height:78px;background:linear-gradient(#e8e8e8 0 12px,var(--top-band) 12px)}
.band-hero{left:0;top:78px;width:1200px;height:264px;background:linear-gradient(var(--hero-red),var(--hero-red-dark))}
.band-footer{left:0;top:975px;width:1200px;height:54px;background:var(--footer-brown)}
.site{left:214px;top:25px;width:772px;height:965px;background:#fff;border-radius:10px;box-shadow:0 0 8px rgba(0,0,0,.35);overflow:hidden}
.site-header{left:0;top:0;width:772px;height:58px;background:linear-gradient(#6a2a16,var(--header-brown))}
.hero{left:0;top:58px;width:772px;height:259px;background:linear-gradient(160deg,#b83b47,var(--hero-red-dark))}
.logo-tab{left:40px;top:-17px;width:244px;height:109px;padding-top:10px;background:linear-gradient(#ffffff,#dcdcdc);border-radius:0 0 16px 16px;box-shadow:0 3px 6px rgba(0,0,0,.4);display:flex;align-items:center;justify-content:center;gap:12px}
.logo-mark{width:24px;height:24px;background:var(--tab-blue)}
.logo-name{font-size:38px;font-weight:700;color:var(--tab-blue)}
.nav{left:318px;top:20px;display:flex;gap:6px}
.nav a{display:block;height:37px;line-height:40px;text-align:center;color:#fff;font-size:13px;text-decoration:none;border-radius:8px 8px 0 0;background:linear-gradient(#4b92dc,var(--tab-blue))}
.nav a.current{background:linear-gradient(#d04c52,var(--tab-red))}
.hero-title{left:36px;top:121px;font-size:30px;font-weight:700;font-style:italic;color:#fff}
.hero-text{left:36px;top:165px;width:320px;font-size:15.5px;line-height:19px;color:#fff}
.dots{left:254px;top:274px;display:flex;gap:4px}
.dots span{width:19px;height:19px;border-radius:50%;background:#5a2716}
.dots span.on{background:#f07112}
.hero-photo{left:387px;top:72px;width:349px;height:226px;border:3px solid #111;background:linear-gradient(180deg,#4a93cf,#5d8aa8 60%,#6f6a62)}
.welcome{left:-4px;top:323px;width:780px;height:54px;background:linear-gradient(#a8392a,#8a2a1c);box-shadow:0 2px 4px rgba(0,0,0,.4)}
.play{left:12px;top:11px;width:33px;height:28px;background:#5b5b5b;border-radius:3px;border:1px solid #2a2a2a}
.welcome-title{left:58px;top:12px;font-size:24px;font-weight:700;color:var(--welcome-orange)}
.quote-pill{left:461px;top:323px;width:308px;height:50px;border-radius:25px;background:linear-gradient(#fdfdfd,#c9c9c9);box-shadow:0 2px 4px rgba(0,0,0,.4);text-align:center;line-height:50px;font-size:24px;font-weight:700;color:#333}
.content{left:0;top:377px;width:772px;height:276px;background:var(--cream)}
.about{left:18px;top:8px;width:446px;height:250px;background:#fff;border-radius:4px;padding:32px 20px 0 32px;font-size:12px;line-height:15px}
.about p{margin-bottom:15px}
.news{left:486px;top:8px;width:263px;height:250px;background:var(--panel-grey);border-radius:4px;border:1px solid #ccc}
.news-btn{left:14px;top:12px;width:235px;height:42px;border-radius:6px;background:linear-gradient(#4a90dc,#1e5aa6);color:#fff;font-size:13.5px;font-weight:700;line-height:42px;padding-left:57px}
.news-btn svg{position:absolute;left:10px;top:6px}
.news-item{left:0;width:261px;height:60px;border-top:1px solid #c9c9c9;padding:0 8px 0 52px;font-size:11.5px;line-height:14px;display:flex;align-items:center}
.news-item svg{position:absolute;left:17px;top:22px}
.projects{left:21px;top:665px;width:728px;height:188px;background:#e0e0e0;border-radius:4px;border:1px solid #cfcfcf}
.projects-inner{left:36px;top:0;width:655px;height:188px;background:#fff}
.projects-head{left:0;top:0;width:655px;height:26px;text-align:center;font-size:14px;font-weight:700;color:var(--accent-red);line-height:26px;letter-spacing:.5px;background:linear-gradient(#fff,#ececec)}
.project{top:26px;width:163px;height:162px;border-left:1px solid #d6d6d6;text-align:center;font-size:12px;line-height:15px;padding-top:14px;background:#f3f3f3}
.project .photo{position:absolute;left:6px;top:52px;width:152px;height:98px}
.testimonials{left:21px;top:865px;width:728px;height:88px;background:var(--panel-grey);border-radius:6px;border:1px solid #c9c9c9}
.testimonial{top:7px;width:226px;font-size:10px;line-height:11.5px}
.testimonial .more{color:var(--link-blue);text-align:right;display:block}
.testimonial .who{color:var(--accent-red);text-align:right;display:block}
.footer-links{left:0;top:996px;width:1200px;text-align:center;color:#fff;font-size:11px}
.footer-links span{margin:0 6px}
.copyright{left:0;top:1012px;width:1200px;text-align:center;color:#fff;font-size:11px}
</style>
</head>
<body>
<div class="abs band-top"></div>
<div class="abs band-hero"></div>
<div class="abs band-footer"></div>

<div class="abs site">
  <div class="abs site-header"></div>
  <div class="abs hero"></div>

  <div class="abs logo-tab"><span class="logo-mark"></span><span class="logo-name">Kestrel</span></div>

  <nav class="abs nav">
    <a class="current" href="#" style="width:83px">Home</a>
    <a href="#" style="width:84px">About Us</a>
    <a href="#" style="width:84px">Testimonials</a>
    <a href="#" style="width:83px">Portfolio</a>
    <a href="#" style="width:83px">Contact</a>
  </nav>

  <h1 class="abs hero-title">KESTREL BUILDER</h1>
  <p class="abs hero-text">Lorem Ipsum dolor sit amet, consecteteur adipiscing elit. Set diem nonum nibh eusmod tincidunt laocreet dolore magna aliguam erat volutpat.</p>
  <div class="abs dots"><span class="on"></span><span></span><span></span><span></span></div>
  <div class="abs hero-photo" role="img" aria-label="Photo of a roofer at work on a house roof"></div>

  <div class="abs content">
    <div class="abs about">
      <p>I am experienced builder in Crawley. Kestrel Construction have been based in Crawley for over 10 years. My team and I are proven, reliable builder based in Crawley. We've come across a lot in our time, so don't hesitate to get in touch about any building job in Crawley.</p>
      <p>I am a friendly, handyman who has built a team of excellent tradesmen based in Crawley. My builders in Crawley have years of experience in kitchen renovation, bathroom renovation, roofing and plumbing. Lot conversions an house restoration.</p>
      <p>Call Kestrel Construction on 0123 555 0198 now to discuss how we can help you . My quotes are always FREE with no obligation.</p>
    </div>
    <div class="abs news">
      <div class="abs news-btn">
        <svg width="30" height="30" viewBox="0 0 30 30"><circle cx="15" cy="15" r="13" fill="#0e2f5c" stroke="#8fb6e6"/><path d="M9 11h12l-6 10z" fill="#8fb6e6"/></svg>
        Latest News &amp; Updates
      </div>
      <div class="abs news-item" style="top:70px"><svg width="14" height="16"><path d="M0 0l14 8-14 8z" fill="#b02a35"/></svg>Kestrel Construction have just finished another fine job in Crawley</div>
      <div class="abs news-item" style="top:130px"><svg width="14" height="16"><path d="M0 0l14 8-14 8z" fill="#b02a35"/></svg>Timber frames seem to be all the range in London. Using the latest in wood tech.</div>
      <div class="abs news-item" style="top:190px"><svg width="14" height="16"><path d="M0 0l14 8-14 8z" fill="#b02a35"/></svg>Just started a 12th century flat conversion. Lots of great finds!</div>
    </div>
  </div>

  <div class="abs welcome">
    <div class="abs play"><svg width="31" height="26"><path d="M12 7l9 6-9 6z" fill="#222"/></svg></div>
    <h2 class="abs welcome-title">Welcome to Kestrel Builders</h2>
  </div>
  <div class="abs quote-pill">Contact Us for A Quote</div>

  <section class="abs projects">
    <div class="abs projects-inner">
      <div class="abs projects-head">LATEST &nbsp; ---- &nbsp; PROJECTS</div>
      <div class="abs project" style="left:0">House restoration in<br>Crawley<div class="photo" role="img" aria-label="Photo of a restored living room" style="background:linear-gradient(#7a5a40,#4a3222)"></div></div>
      <div class="abs project" style="left:164px">Loft Conversion near<br>Crawley<div class="photo" role="img" aria-label="Photo of a converted loft dining area" style="background:linear-gradient(#8a6a4e,#d8c8b0)"></div></div>
      <div class="abs project" style="left:328px">Home painting and<br>decoration in Crawley<div class="photo" role="img" aria-label="Photo of a freshly decorated interior" style="background:linear-gradient(#e6d4bc,#d4a770)"></div></div>
      <div class="abs project" style="left:492px">Beautiful house extension<br>in Crawley<div class="photo" role="img" aria-label="Photo of a kitchen in a house extension" style="background:linear-gradient(#b8b0a8,#e4ddd5)"></div></div>
    </div>
  </section>

  <section class="abs testimonials">
    <div class="abs testimonial" style="left:12px">“Kestrel Construction are the best builders Crawley. They are experts in all areas of house building and I am extremely satisfied with my new loft conversion”<span class="more">more</span><span class="who">Mr. Halloran</span></div>
    <div class="abs testimonial" style="left:252px">“I rarely write refernces for anyone, but Kestrel Construction builders in Crawley are Outstanding. They restored my Crawley home to avery high specification and the team are very approchable and friendly.”<span class="more">more</span><span class="who">Mr. Halloran</span></div>
    <div class="abs testimonial" style="left:492px">“I found Kestrel Construction in Crawley through their amazing website and I made my decision to ask for a quote once I saw excellent testimonials,...”<span class="more">more</span><span class="who">Mr. Halloran</span></div>
  </section>
</div>

<div class="abs footer-links">Home<span>I</span>About Us<span>I</span>Testimonials<span>I</span>Portfolio<span>I</span>Contact</div>
<div class="abs copyright">Copyright © 2011. kestrelbuilders.com. All rights reserved.</div>
</body>
</html>
```